Business Card Design

I am a GP with interest in Dermatology and Aesthetic Medicin, performing Botulinum Toxin Type A and Dermal Fillers treatmets in Cosmetic Dermatology clinic.

I am looking for a white colour, good quality white paper card may be of some special texture with black calligraphic writing but easy to read and not to wiggly- professional- looking.

Really appreciate your help.

Milena

Contact Information for Business Card

Cosmetic Dermatology Clinic

Dr Milena Ravitskaya, MBBS, MRCGP, DPD

Tel: 07915 462 170
milena@medpractice-mail.co.uk

```html
<!DOCTYPE html>
<html lang="en">
<head>
<meta charset="utf-8">
<title>Cosmetic Dermatology Clinic – Business Card</title>
<link href="https://fonts.googleapis.com/css2?family=Quicksand:wght@300;400;500&display=swap" rel="stylesheet">
<style>
  :root {
    --backdrop: #e9e9ea;
    --paper: #fbfbfb;
    --ink-dark: #4a4a4a;
    --ink-mid: #6a6a6a;
    --ink-soft: #8e8e8e;
    --rule: #5a5a5a;
    --card-shadow: rgba(0, 0, 0, 0.12);
  }
  * { margin: 0; padding: 0; box-sizing: border-box; }
  html, body {
    width: 1200px;
    height: 720px;
    overflow: hidden;
    background: var(--backdrop);
    font-family: "Quicksand", sans-serif;
  }
  .canvas {
    position: relative;
    width: 1200px;
    height: 720px;
  }
  .card {
    position: absolute;
    top: 211px;
    width: 520px;
    height: 297px;
    background: var(--paper);
    box-shadow: 0 6px 18px var(--card-shadow);
    overflow: hidden;
  }
  .card--front { left: 50px; }
  .card--back { left: 630px; }

  .bar {
    display: block;
    width: 5px;
    height: 20px;
    background: var(--ink-mid);
    flex: none;
  }
  .rule {
    position: absolute;
    height: 1.5px;
    background: var(--rule);
  }

  /* Front */
  .front-heading {
    position: absolute;
    left: 0;
    width: 520px;
    top: 98px;
    display: flex;
    align-items: center;
    justify-content: center;
    gap: 10px;
  }
  .front-title {
    font-size: 28px;
    font-weight: 300;
    letter-spacing: 1px;
    color: var(--ink-soft);
    white-space: nowrap;
    line-height: 36px;
  }
  .card--front .rule { left: 68px; width: 384px; top: 146px; }
  .front-signature {
    position: absolute;
    right: 72px;
    top: 160px;
    text-align: right;
    color: var(--ink-soft);
  }
  .front-name {
    font-size: 20px;
    font-weight: 300;
    letter-spacing: 0.8px;
    line-height: 28px;
  }
  .front-credentials {
    font-size: 9px;
    font-weight: 400;
    letter-spacing: 0.6px;
    margin-right: 24px;
  }

  /* Back */
  .card--back .bar--corner { position: absolute; left: 470px; top: 36px; }
  .back-heading {
    position: absolute;
    left: 38px;
    top: 91px;
    display: flex;
    align-items: center;
    gap: 11px;
  }
  .back-name {
    font-size: 22px;
    font-weight: 500;
    letter-spacing: 0.8px;
    color: var(--ink-dark);
    white-space: nowrap;
    line-height: 30px;
  }
  .back-name .credentials {
    font-size: 9px;
    font-weight: 400;
    letter-spacing: 0.5px;
    color: var(--ink-mid);
    margin-left: 6px;
  }
  .back-speciality {
    position: absolute;
    left: 70px;
    width: 400px;
    top: 125px;
    text-align: center;
    font-size: 10.5px;
    font-weight: 400;
    line-height: 15px;
    letter-spacing: 0.4px;
    color: var(--ink-mid);
  }
  .card--back .rule { left: 60px; width: 410px; top: 172px; }
  .contact {
    position: absolute;
    left: 60px;
    width: 410px;
    top: 186px;
    display: flex;
    flex-direction: column;
    align-items: center;
    color: var(--ink-mid);
  }
  .contact-icon {
    width: 15px;
    height: 15px;
    display: block;
    margin-bottom: 3px;
  }
  .contact-line {
    font-size: 15px;
    font-weight: 400;
    letter-spacing: 1px;
    margin-bottom: 8px;
  }
</style>
</head>
<body>
<main class="canvas">

  <section class="card card--front" aria-label="Business card front">
    <div class="front-heading">
      <span class="bar"></span>
      <h1 class="front-title">Cosmetic Dermatology Clinic</h1>
      <span class="bar"></span>
    </div>
    <span class="rule"></span>
    <div class="front-signature">
      <p class="front-name">Dr Milena Ravitskaya</p>
      <p class="front-credentials">MBBS, MRCGP, DPD</p>
    </div>
  </section>

  <section class="card card--back" aria-label="Business card back">
    <span class="bar bar--corner"></span>
    <div class="back-heading">
      <span class="bar"></span>
      <h2 class="back-name">Dr Milena Ravitskaya<span class="credentials">MBBS, MRCGP, DPD</span></h2>
    </div>
    <p class="back-speciality">Dermatology and Aesthetic Medicine,<br>Botulinum Toxin Type A and Dermal Fillers treatmets</p>
    <span class="rule"></span>
    <div class="contact">
      <svg class="contact-icon" viewBox="0 0 16 16" aria-hidden="true">
        <circle cx="8" cy="8" r="8" fill="#4a4a4a"/>
        <path d="M5.3 4.2c.3-.2.7-.2.9.1l.9 1.3c.2.3.1.6-.1.8l-.5.4c.4.9 1.1 1.6 2 2l.4-.5c.2-.2.6-.3.8-.1l1.3.9c.3.2.3.6.1.9l-.5.6c-.4.4-1 .5-1.6.3C7.1 10.2 5.8 8.9 5 7.1c-.2-.6-.1-1.2.3-1.6z" fill="#fbfbfb"/>
      </svg>
      <p class="contact-line">07915 462 170</p>
      <svg class="contact-icon" viewBox="0 0 16 16" aria-hidden="true">
        <circle cx="8" cy="8" r="8" fill="#4a4a4a"/>
        <rect x="4" y="5.2" width="8" height="5.6" fill="none" stroke="#fbfbfb" stroke-width="1"/>
        <path d="M4 5.4 8 8.6 12 5.4" fill="none" stroke="#fbfbfb" stroke-width="1"/>
      </svg>
      <p class="contact-line">milena@medpractice-mail.co.uk</p>
    </div>
  </section>

</main>
</body>
</html>
```